Stationary for I.T. company
DuskVale
Stationary for I.T. company - Information Technology
Creative Brief
Bright & Fun-filled
Ray Olsen
Director
PO Box 4172 Marlow ACT 2913
ops@duskva.le
duskva.le
Eye catching - display the DuskVale logo with either the red N with the white text or the white only logo on a background with either bold colours, dark greys or black. Open to other concepts or suggestions if they are eye catching
brimlow brimlow
Thank you everyone for your efforts. We may ask a couple more questons to relevant designers - but we plan to decide in the next 24 to 48 hours. Thanks again.
Thanks everyone for your submissions so far.. 266 designs is much much more than we were expecting. To help everyone understand where we are going and what we are looking for we will start eliminating some designs tonight. With that, we will probably start to give out a couple (maybe 3) 5 star ratings. These will indicate the current leading designs. We will probably also redo most of the star ratings out there to better give designers a better understanding of what we like. Please note that there is several people looking at these designs, so star rating may go up and down a little... but be assured if it has stars, we like it, or like some concepts in it.
We will aim to provide every designer feedback and stars (so yes - it may look like we rate a lot of things highly). 4 stars will generally be used to indicate the favorite submission of a designer, and 5 will only be used when we start eliminating designs.
tallfern tallfern
Check your private messages...
Also looking for letter head, invoice, envelope, notepad templates, presentation folder in addition to business card design. Thanks.
Amendment to the design brief - we will also accept a white background for the back of the business card

```html
<!DOCTYPE html>
<html lang="en">
<head>
<meta charset="utf-8">
<title>DuskVale Stationery</title>
<link rel="stylesheet" href="https://fonts.googleapis.com/css2?family=Exo+2:wght@400;600&family=Open+Sans:wght@400;600&display=swap">
<style>
:root{
  --backdrop:#8c8c8c;
  --ink:#1a1a1a;
  --night:#111111;
  --night-soft:#2a2a2a;
  --paper:#ffffff;
  --red:#c4161c;
  --red-dark:#7d0d10;
  --grey-line:#d6d6d6;
  --text-grey:#666666;
}
*{box-sizing:border-box;margin:0;padding:0}
html,body{width:1200px;height:490px;overflow:hidden}
body{background:radial-gradient(ellipse at 50% 45%,#a4a4a4 0%,var(--backdrop) 70%,#6e6e6e 100%);position:relative;font-family:"Open Sans",sans-serif;color:var(--ink)}
.piece{position:absolute;box-shadow:0 3px 8px rgba(0,0,0,.35)}
.brand{display:flex;align-items:center;gap:5px;font-family:"Exo 2",sans-serif;font-weight:600;white-space:nowrap}
.brand .dot{width:var(--d,14px);height:var(--d,14px);border-radius:50%;background:var(--red);flex:none}
.brand.on-dark{color:var(--paper)}
.brand.on-light{color:var(--ink)}
.faint-disc{position:absolute;border-radius:50%;background:rgba(196,22,28,.08)}
.faint-disc.dark{background:rgba(255,255,255,.05)}
.red-band{position:absolute;left:0;right:0;background:linear-gradient(90deg,var(--red-dark),var(--red))}
.dark-band{position:absolute;left:0;right:0;background:linear-gradient(180deg,var(--night-soft),var(--night))}

/* folder */
.folder-cover{left:14px;top:67px;width:226px;height:401px;background:linear-gradient(160deg,#2b2b2b,var(--night) 60%);overflow:hidden}
.folder-cover .brand{position:absolute;left:62px;top:108px;font-size:21px}
.folder-inside{left:240px;top:67px;width:216px;height:401px;background:var(--paper);overflow:hidden}
.folder-inside .brand{position:absolute;left:46px;top:150px;font-size:17px}
.folder-pocket{left:14px;top:348px;width:442px;height:120px;background:linear-gradient(180deg,#262626,var(--night));}
.folder-pocket .brand{position:absolute;left:214px;top:72px;font-size:0;--d:20px}
.folder-flap{position:absolute;left:0;width:14px;height:40px;background:var(--paper)}

/* disc */
.disc{left:482px;top:108px;width:84px;height:84px;border-radius:50%;background:radial-gradient(circle,#bbb 0 7px,var(--paper) 8px 22px,#f2f2f2 23px);overflow:hidden}
.disc .brand{position:absolute;left:22px;top:34px;font-size:9px;--d:8px}

/* compliment slip */
.slip{left:570px;top:90px;width:140px;height:62px;background:var(--paper);overflow:hidden}
.slip .brand{position:absolute;left:10px;top:10px;font-size:14px;--d:14px}

/* business cards */
.card{width:120px;height:66px;overflow:hidden;font-size:5.5px;line-height:1.4}
.card .brand{position:absolute}
.card-white{left:736px;top:95px;background:var(--paper)}
.card-white .brand{left:10px;top:10px;font-size:11px;--d:10px}
.card-white .details{position:absolute;left:10px;bottom:14px;color:var(--text-grey)}
.card-dark{background:linear-gradient(160deg,#2e2e2e,var(--night))}
.card-dark .details{position:absolute;left:10px;bottom:12px;color:#cfcfcf}
.card-dark.a{left:736px;top:170px}
.card-dark.a .brand{left:30px;top:18px;font-size:13px;--d:12px}
.card-dark.b{left:866px;top:170px}
.card-dark.b .brand{left:10px;top:10px;font-size:10px;--d:10px}
.card-dark.c{left:936px;top:68px;width:116px;height:40px}
.card-dark.c .brand{left:10px;top:12px;font-size:11px;--d:10px}
.card-white.d{left:1066px;top:68px;width:116px;height:40px}
.card-white.d .brand{top:12px}
.name{font-weight:600;color:inherit;font-size:6.5px}

/* letterheads */
.sheet{width:198px;height:235px;top:240px;background:var(--paper);overflow:hidden}
.sheet .brand{position:absolute;left:14px;top:14px;font-size:12px;--d:12px}
.invoice{left:498px}
.letter{left:716px}
.invoice-table{position:absolute;left:14px;top:42px;width:118px;border-collapse:collapse;font-size:5px;color:var(--text-grey)}
.invoice-table td{border:1px solid var(--grey-line);padding:1px 3px;height:9px}
.invoice-title{position:absolute;right:14px;top:18px;font-size:8px;font-weight:600;color:var(--red)}
.body-lines{position:absolute;left:14px;right:14px;top:72px}
.body-lines span{display:block;height:1px;background:#ececec;margin-bottom:9px}
.sheet-foot{position:absolute;left:14px;bottom:8px;font-size:4.5px;color:var(--text-grey)}

/* envelopes */
.envelope-front{left:936px;top:240px;width:250px;height:115px;background:var(--paper);overflow:hidden}
.envelope-front .brand{position:absolute;left:14px;top:12px;font-size:11px;--d:10px}
.envelope-front .address{position:absolute;left:104px;top:58px;font-size:5.5px;color:var(--text-grey);line-height:1.5}
.envelope-back{left:936px;top:384px;width:250px;height:96px;background:var(--paper);overflow:hidden}
.envelope-back .brand{position:absolute;left:110px;top:66px;font-size:0;--d:12px}
</style>
</head>
<body>

<!-- presentation folder -->
<div class="piece folder-cover">
  <div class="faint-disc dark" style="left:40px;top:190px;width:220px;height:220px"></div>
  <div class="red-band" style="top:0;height:3px"></div>
  <div class="brand on-dark" style="--d:20px"><span class="dot"></span>DuskVale</div>
</div>
<div class="piece folder-inside">
  <div class="faint-disc" style="left:30px;top:200px;width:170px;height:170px"></div>
  <div class="red-band" style="top:168px;height:3px;left:130px"></div>
  <div class="brand on-light" style="--d:18px"><span class="dot"></span>DuskVale</div>
</div>
<div class="piece folder-pocket">
  <div class="red-band" style="top:0;height:3px"></div>
  <div class="brand on-dark"><span class="dot"></span></div>
</div>
<div class="folder-flap" style="top:150px"></div>
<div class="folder-flap" style="top:300px"></div>

<!-- disc -->
<div class="piece disc">
  <div class="brand on-light"><span class="dot"></span>DuskVale</div>
</div>

<!-- compliment slip -->
<div class="piece slip">
  <div class="brand on-light"><span class="dot"></span>DuskVale</div>
  <div class="dark-band" style="bottom:0;height:16px"></div>
  <div class="red-band" style="bottom:16px;height:2px;left:70px"></div>
</div>

<!-- business cards -->
<div class="piece card card-white" style="position:absolute">
  <div class="brand on-light"><span class="dot"></span>DuskVale</div>
  <div class="details"><span class="name" style="color:var(--ink)">Ray Olsen</span><br>Director<br>ops@duskva.le</div>
  <div class="dark-band" style="bottom:0;height:8px"></div>
  <div class="red-band" style="bottom:8px;height:2px;left:60px"></div>
</div>
<div class="piece card card-dark a">
  <div class="brand on-dark"><span class="dot"></span>DuskVale</div>
  <div class="red-band" style="bottom:0;height:3px"></div>
</div>
<div class="piece card card-dark b">
  <div class="brand on-dark"><span class="dot"></span>DuskVale</div>
  <div class="details"><span class="name">Ray Olsen</span><br>PO Box 4172 Marlow ACT 2913<br>duskva.le</div>
  <div class="red-band" style="bottom:0;height:3px"></div>
</div>
<div class="piece card card-dark c">
  <div class="brand on-dark"><span class="dot"></span>DuskVale</div>
  <div class="red-band" style="bottom:0;height:2px"></div>
</div>
<div class="piece card card-white d">
  <div class="brand on-light"><span class="dot"></span>DuskVale</div>
  <div class="dark-band" style="bottom:0;height:6px"></div>
</div>

<!-- invoice -->
<div class="piece sheet invoice">
  <div class="brand on-light"><span class="dot"></span>DuskVale</div>
  <div class="invoice-title">Invoice</div>
  <table class="invoice-table">
    <tr><td>Date</td><td></td></tr>
    <tr><td>Item</td><td>Qty</td></tr>
    <tr><td></td><td></td></tr>
    <tr><td>Amount</td><td></td></tr>
    <tr><td>Total</td><td></td></tr>
  </table>
  <div class="faint-disc" style="left:40px;top:130px;width:120px;height:120px"></div>
  <div class="sheet-foot">PO Box 4172 Marlow ACT 2913 · duskva.le</div>
  <div class="red-band" style="bottom:0;height:3px"></div>
</div>

<!-- letterhead -->
<div class="piece sheet letter">
  <div class="brand on-light"><span class="dot"></span>DuskVale</div>
  <div class="body-lines"><span></span><span></span><span></span><span></span><span></span><span></span></div>
  <div class="faint-disc" style="left:40px;top:130px;width:120px;height:120px"></div>
  <div class="sheet-foot">PO Box 4172 Marlow ACT 2913 · ops@duskva.le</div>
  <div class="red-band" style="bottom:0;height:3px"></div>
</div>

<!-- envelopes -->
<div class="piece envelope-front">
  <div class="brand on-light"><span class="dot"></span>DuskVale</div>
  <div class="address">Ray Olsen<br>PO Box 4172 Marlow ACT 2913</div>
  <div class="red-band" style="bottom:0;height:3px"></div>
</div>
<div class="piece envelope-back">
  <svg width="250" height="96" viewBox="0 0 250 96" style="position:absolute;left:0;top:0">
    <polygon points="0,0 250,0 125,70" fill="#151515"/>
    <polyline points="0,96 110,48" stroke="#e2e2e2" fill="none"/>
    <polyline points="250,96 140,48" stroke="#e2e2e2" fill="none"/>
    <polygon points="0,0 250,0 250,3 0,3" fill="#c4161c"/>
  </svg>
  <div class="brand on-light"><span class="dot"></span></div>
</div>

</body>
</html>
```